We need a brand new Employee Handbook for a team of aged and disability support workers

We need an employee handbook designed for our team of aged and disability support workers.
We provide a range of disability and aged care services to persons in our region.
We are a small business, providing unique and personalised support to vulnerable people. We actually provide choice and control to our clients - something the bigger agencies say they do but don't follow through with.
We aim to be an employer of choice - providing a workplace that supports our staff personally and professionally.
We would like to see the colours gold, yellow, black, grey and white.
We would like to incorporate photos of our current team members and stock photos of fun teams, persons with a disability, elderly and carers in the community and home.
The final design should communicate a fun, supportive team offering growth and opportunity.

```html
<!DOCTYPE html>
<html lang="en">
<head>
<meta charset="utf-8">
<title>Marlow Care – Employee Handbook Covers</title>
<link rel="stylesheet" href="https://fonts.googleapis.com/css2?family=Sniglet:wght@400;800&family=Open+Sans:wght@400;600&display=swap">
<style>
  :root {
    --stage: #6f6f6f;
    --paper: #ffffff;
    --sky-light: #f4f3f2;
    --sky-mid: #d9d6d3;
    --sky-deep: #9e9995;
    --gold: #d9bd55;
    --gold-deep: #c9a93a;
    --ink: #3a3a3a;
    --ring: #8a8a8a;
    --photo-green: #6f8a3c;
    --photo-warm: #c9a46a;
    --photo-stone: #b9a27c;
  }
  * { box-sizing: border-box; margin: 0; padding: 0; }
  html, body {
    width: 900px; height: 1200px; overflow: hidden;
    background: var(--stage);
    font-family: "Open Sans", Arial, sans-serif;
  }
  .canvas {
    width: 900px; height: 1200px;
    display: flex; flex-direction: column; align-items: center;
    justify-content: center; gap: 48px;
  }
  .cover {
    position: relative; width: 780px; height: 520px;
    background: var(--paper); overflow: hidden;
    box-shadow: 0 10px 24px rgba(0,0,0,.35);
  }
  .front-cover {
    background:
      radial-gradient(ellipse 60% 30% at 20% 0%, var(--sky-mid), transparent 70%),
      radial-gradient(ellipse 50% 25% at 75% 0%, var(--sky-light), transparent 70%),
      var(--paper);
  }
  .photo-frame { position: absolute; left: 340px; top: -90px; width: 520px; height: 520px; }
  .brand-name {
    position: absolute; left: 70px; top: 70px;
    font-family: "Open Sans", Arial, sans-serif; font-weight: 600;
    font-size: 40px; color: var(--gold-deep); letter-spacing: 0.5px;
  }
  .headline { position: absolute; left: 70px; top: 150px; font-family: "Sniglet", "Comic Sans MS", sans-serif; line-height: .95; }
  .headline-your { display: block; font-size: 118px; color: var(--gold); }
  .headline-life { display: block; font-size: 104px; color: var(--ink); margin-left: 60px; }
  .subline {
    position: absolute; left: 70px; top: 395px;
    font-family: "Open Sans", Arial, sans-serif; font-size: 27px; color: var(--ink);
  }
  .subline-rule { position: absolute; left: 150px; top: 440px; }
  .web-address {
    position: absolute; left: 92px; top: 465px;
    font-size: 12px; letter-spacing: 4px; color: var(--ink);
  }
  .back-cover {
    background: linear-gradient(160deg, var(--sky-deep) 0%, var(--sky-mid) 30%, var(--sky-light) 60%, var(--paper) 85%);
  }
  .back-brand {
    position: absolute; left: 250px; top: 370px;
    font-weight: 600; font-size: 42px; color: var(--gold-deep);
  }
  .back-web {
    position: absolute; left: 275px; top: 440px;
    font-size: 12px; letter-spacing: 4px; color: var(--ink);
  }
</style>
</head>
<body>
<main class="canvas">
  <section class="cover front-cover" aria-label="Front cover">
    <svg class="photo-frame" viewBox="0 0 520 520" xmlns="http://www.w3.org/2000/svg">
      <defs>
        <linearGradient id="photoTone" x1="0" y1="0" x2="1" y2="1">
          <stop offset="0" stop-color="var(--photo-stone)"/>
          <stop offset=".45" stop-color="var(--photo-warm)"/>
          <stop offset="1" stop-color="var(--photo-green)"/>
        </linearGradient>
      </defs>
      <circle cx="260" cy="260" r="250" fill="none" stroke="var(--ring)" stroke-width="3"/>
      <path d="M 70 380 A 225 225 0 0 0 470 330" fill="none" stroke="var(--gold)" stroke-width="14" stroke-linecap="round"/>
      <circle cx="275" cy="250" r="222" fill="url(#photoTone)" role="img"
              aria-label="Photo of a carer smiling with an elderly man in a wheelchair in a garden"/>
    </svg>
    <div class="brand-name">Marlow Care</div>
    <h1 class="headline">
      <span class="headline-your">Your</span>
      <span class="headline-life">Life</span>
    </h1>
    <p class="subline">your plan , your way</p>
    <svg class="subline-rule" width="120" height="10" viewBox="0 0 120 10">
      <path d="M4 6 Q60 1 116 5" stroke="var(--gold)" stroke-width="5" fill="none" stroke-linecap="round"/>
    </svg>
    <p class="web-address">www.marlowcare.com</p>
  </section>

  <section class="cover back-cover" aria-label="Back cover">
    <div class="back-brand">Marlow Care</div>
    <p class="back-web">www.marlowcare.com</p>
  </section>
</main>
</body>
</html>
```